Professional Music Editor Needs a Book Cover Design

I need a book cover design for a series of books which will include excerpts from symphonic pieces required for auditions in professional symphony orchestras. The books will contain text and a lot of music examples. The book will be published in a Brivo and eLeafs version, to be used mainly on an zTab, but will be also available in print in A4 size. The cover may incorporate notation or/and violin images.

The text on the cover should include:

Author: Teodor Markelin D.M.A.
Series: Morning Scales Concert Passages for Violin
Title: Anselm Berlicke, Pale Tower Op. 20, measures 1-62
Updates

Thank you so much for the submitted projects so far! I have uploaded one more photo, which I think may be a good element to use. If you decide to incorporate it, please use just the violin from the photo, not the person. 

And one more thing: I would like the design to be modern, rather than traditional.

Thanks a lot for your work!

Target Market(s)

The target customers of this edition are college students who are going to use the book to prepare for auditions for professional orchestras.

Industry/Entity Type

It Professional

Colors
ffffff

```html
<!DOCTYPE html>
<html lang="en">
<head>
<meta charset="utf-8">
<title>Morning Scales Concert Passages for Violin – Book Cover</title>
<link rel="stylesheet" href="https://fonts.googleapis.com/css2?family=Cinzel:wght@400;500&family=Crimson+Text&display=swap">
<style>
  :root {
    --spine-brown: #5e3522;
    --accent-rust: #7b3a21;
    --paper: #ffffff;
    --ink: #111111;
    --light-ink: #f3ece6;
  }
  * { margin: 0; padding: 0; box-sizing: border-box; }
  html, body { width: 1200px; height: 849px; overflow: hidden; background: var(--paper); }
  .cover { position: relative; width: 1200px; height: 849px; }
  .back-panel {
    position: absolute; left: 0; top: 0; width: 600px; height: 849px;
    background: var(--spine-brown); color: var(--light-ink); text-align: center;
  }
  .front-panel { position: absolute; left: 600px; top: 0; width: 600px; height: 849px; background: var(--paper); text-align: center; }
  .line { position: absolute; left: 0; width: 100%; white-space: nowrap; }
  .caps { font-family: "Cinzel", serif; }
  .serif { font-family: "Crimson Text", serif; }

  .back-author { top: 318px; font-size: 14px; letter-spacing: 0.5px; }
  .back-series { top: 366px; font-size: 15px; }
  .back-composer { top: 388px; font-size: 23px; font-weight: 500; }
  .back-title { top: 418px; font-size: 22px; }
  .back-measures { top: 446px; font-size: 22px; }

  .front-author { top: 28px; left: 10px; font-size: 30px; color: var(--accent-rust); letter-spacing: 1px; }
  .front-series { top: 86px; left: 10px; font-size: 40px; line-height: 46px; color: var(--ink); }
  .front-composer { top: 660px; left: 10px; font-size: 45px; color: var(--accent-rust); }
  .front-title { top: 716px; left: 10px; font-size: 44px; color: var(--ink); }
  .front-measures { top: 766px; left: 10px; font-size: 44px; color: var(--ink); }

  .hero-art { position: absolute; left: 588px; top: 180px; width: 612px; height: 470px; }
</style>
</head>
<body>
<div class="cover">
  <section class="back-panel">
    <p class="line caps back-author">Teodor Markelin D.M.A.</p>
    <p class="line serif back-series">Morning Scales Concert Passages for Violin</p>
    <p class="line caps back-composer">Anselm Berlicke</p>
    <p class="line caps back-title">Pale Tower Op. 20</p>
    <p class="line caps back-measures">Measures 1-62</p>
  </section>

  <section class="front-panel">
    <p class="line caps front-author">Teodor Markelin D.M.A.</p>
    <h1 class="line serif front-series" style="font-weight:400">Morning Scales Concert<br>Passages for Violin</h1>
    <p class="line caps front-composer">Anselm Berlicke</p>
    <p class="line caps front-title">Pale Tower Op. 20</p>
    <p class="line caps front-measures">Measures 1-62</p>
  </section>

  <svg class="hero-art" viewBox="0 0 612 470" role="img" aria-label="Photograph of a violin scroll and pegbox over a large slanted staff of printed music notation">
    <defs>
      <radialGradient id="scrollTone" cx="0.22" cy="0.3" r="0.75">
        <stop offset="0" stop-color="#8a4a1f"/>
        <stop offset="0.35" stop-color="#5a2f16"/>
        <stop offset="0.7" stop-color="#c9b8a8"/>
        <stop offset="1" stop-color="#ffffff"/>
      </radialGradient>
    </defs>
    <rect width="612" height="470" fill="url(#scrollTone)"/>
  </svg>
</div>
</body>
</html>
```